my personal cards just intrducing my self

Massage Therapy to get my name out their

Target Market(s)

40 year olds who enjoy massage

Industry/Entity Type

Massage

Contact Information for Business Card

Marcus L Tolhaven
LMT-Licensed Massage Therapist
*Swedish *Deep Tissue *Prenatal
*Reflexology *Chair and more

(738)-462-1937
marcustolhaven@mailbrook.net

Font styles to use
Serif

Colors
0456a4
6b449b

```html
<!DOCTYPE html>
<html lang="en">
<head>
<meta charset="utf-8">
<title>Marcus L Tolhaven — Business Card</title>
<link rel="stylesheet" href="https://fonts.googleapis.com/css2?family=Gabriela&family=Dancing+Script:wght@600&display=swap">
<style>
  :root {
    --card-blue: #1f62a0;
    --card-purple: #6f5199;
    --name-purple: #8a6cc0;
    --ink-light: #f4f1fa;
    --backdrop: #ececec;
  }
  * { margin: 0; padding: 0; box-sizing: border-box; }
  html, body {
    width: 1200px;
    height: 900px;
    overflow: hidden;
    background: var(--backdrop);
  }
  .stage { position: relative; width: 1200px; height: 900px; }

  .card {
    position: absolute;
    left: 325px;
    width: 552px;
    height: 356px;
    border-radius: 22px;
    background: var(--card-blue);
    overflow: hidden;
    box-shadow: 0 4px 12px rgba(0,0,0,0.18);
  }
  .card-front { top: 63px; border: 2px solid var(--card-purple); }
  .card-back { top: 434px; }

  .front-name {
    position: absolute;
    right: 24px;
    top: 150px;
    font-family: "Dancing Script", cursive;
    font-weight: 600;
    font-size: 40px;
    color: var(--name-purple);
    text-shadow: 0 0 2px #fff, 0 0 3px #fff, 0 0 4px #e8ddff;
    white-space: nowrap;
  }

  .back-heading {
    position: absolute;
    left: 0;
    width: 100%;
    top: 94px;
    text-align: center;
    font-family: "Gabriela", serif;
    color: var(--ink-light);
  }
  .back-name { font-size: 20px; letter-spacing: 0.3px; padding-left: 10px; }
  .back-title { font-size: 15px; margin-top: 4px; padding-left: 22px; }

  .service-list {
    position: absolute;
    top: 174px;
    left: 20px;
    right: 20px;
    display: flex;
    justify-content: space-between;
    list-style: none;
    font-family: "Gabriela", serif;
    font-size: 12.5px;
    color: var(--ink-light);
  }
  .service-list li { display: flex; align-items: center; gap: 4px; white-space: nowrap; }
  .service-list li::before {
    content: "";
    width: 10px;
    height: 10px;
    background: var(--card-purple);
    border: 1px solid #b9a6d8;
  }

  .contact-band {
    position: absolute;
    left: 0;
    top: 228px;
    width: 100%;
    height: 100px;
    background: var(--card-purple);
    font-family: "Gabriela", serif;
    font-size: 14px;
    color: var(--ink-light);
  }
  .contact-line {
    position: absolute;
    left: 184px;
    display: flex;
    align-items: center;
    gap: 7px;
  }
  .contact-phone { top: 24px; }
  .contact-email { top: 57px; }
  .contact-line svg { width: 15px; height: 15px; flex: none; }
</style>
</head>
<body>
<main class="stage">
  <section class="card card-front">
    <p class="front-name">Marcus L Tolhaven</p>
  </section>

  <section class="card card-back">
    <header class="back-heading">
      <h1 class="back-name">MARCUS L TOLHAVEN</h1>
      <p class="back-title">LMT-Licensed Massage Therapist</p>
    </header>

    <ul class="service-list">
      <li>SWEDISH</li>
      <li>DEEP TISSUE</li>
      <li>PRENATAL</li>
      <li>REFLEXOLOGY</li>
      <li>CHAIR AND MORE</li>
    </ul>

    <div class="contact-band">
      <p class="contact-line contact-phone">
        <svg viewBox="0 0 16 16" aria-hidden="true">
          <circle cx="8" cy="8" r="8" fill="#f4f1fa"/>
          <path d="M5.2 3.8l1.3-.3.9 2-.8.8c.4 1 1.1 1.7 2.1 2.1l.8-.8 2 .9-.3 1.3c-.2.6-.8.9-1.4.8-2.7-.5-4.5-2.3-5-5-.1-.6.2-1.2.8-1.4z" fill="#6f5199"/>
        </svg>
        (738)-462-1937
      </p>
      <p class="contact-line contact-email">
        <svg viewBox="0 0 16 16" aria-hidden="true">
          <circle cx="8" cy="8" r="8" fill="#f4f1fa"/>
          <rect x="4" y="5.2" width="8" height="5.6" rx="0.6" fill="#6f5199"/>
          <path d="M4.3 5.6L8 8.4l3.7-2.8" fill="none" stroke="#f4f1fa" stroke-width="0.9"/>
        </svg>
        marcustolhaven@mailbrook.net
      </p>
    </div>
  </section>
</main>
</body>
</html>
```